Anzeigengestaltung für Teppichwäscherei
Zielgruppe
Wir sind eine Teppichwäscherei mit sitz in Recklinghausen.
Wir waschen alle arten von Teppichen vorallem hochwertige perser und designer teppiche.
Zu unserem service gehört auch die Teppichreparatur und restauration von alten und antiken stücken.
unsere zielgruppe sind private haushalte ab 40+ die auch ein teppich zuhause haben.
Aufgabenstellung
es soll modern kreative und auffällig sein aber nicht so das ältere kunden abgeschreckt sind.
folgende sachen müssen drin sein - Teppichreinigung & Teppichreparatur - Kostenlose (gratis ) Abholung und lieferung -
Format: 2sp./100mm & 3sp./100mm & 4sp./225mm
-Normalwäsche statt 19€ jetzt 16 €
-Vollwäsche statt 27€ jetzt 24 €
-Seidenwäsche statt 49€ jetzt 40 €
angebot gilt nur 5 Tage
vom xx.xx.xx bis zum xx.xx.xx

```html
<!DOCTYPE html>
<html lang="de">
<head>
<meta charset="utf-8">
<title>KWR Teppichservice – Anzeige</title>
<link rel="stylesheet" href="https://fonts.googleapis.com/css2?family=Bebas+Neue&family=Montserrat:wght@400;700;800&display=swap">
<style>
  :root {
    --navy: #243d63;
    --blue: #0b4fc4;
    --blue-deep: #0a35a0;
    --blue-light: #2a74dd;
    --tile: #dce9f6;
    --red: #e41f28;
    --white: #ffffff;
    --page: #9a9a9a;
    --rug: #a8403f;
    --rug-dark: #6e2a2c;
  }
  * { margin: 0; padding: 0; box-sizing: border-box; }
  html, body { width: 1200px; height: 1117px; overflow: hidden; background: var(--page); }
  .stage { position: relative; width: 1200px; height: 1117px; }
  .ad {
    position: absolute; left: 75px; top: 191px;
    width: 1740px; height: 1224px;
    transform: scale(0.6036); transform-origin: 0 0;
    background: var(--white); overflow: hidden;
    font-family: "Montserrat", sans-serif;
  }
  .hero-photo {
    position: absolute; left: 560px; top: 0; width: 1180px; height: 525px;
    background: linear-gradient(160deg, #b9b3ae 0%, var(--rug) 35%, #b55250 60%, var(--rug-dark) 100%);
  }
  .brand-panel { position: absolute; left: 0; top: 0; width: 760px; height: 525px; }
  .brand-name {
    position: absolute; left: 124px; top: 42px; width: 464px; height: 464px;
    border-radius: 50%; background: var(--blue-deep);
    display: flex; align-items: center; justify-content: center; text-align: center;
    color: var(--white); font-weight: 800; font-size: 52px; line-height: 1.2;
  }
  .photo-round {
    position: absolute; width: 456px; height: 456px; border-radius: 50%;
    border: 24px solid var(--white); top: 305px;
  }
  .photo-round.one { left: 796px; background: radial-gradient(circle at 45% 40%, #e8e4e2 0%, #c75a55 40%, var(--rug-dark) 100%); }
  .photo-round.two { left: 1248px; background: radial-gradient(circle at 45% 35%, #8a8a88 0%, #d9cfcb 35%, #b8403c 65%, var(--rug-dark) 100%); }
  .headline {
    position: absolute; left: 112px; top: 552px;
    font-family: "Bebas Neue", sans-serif; color: var(--navy);
    font-size: 106px; line-height: 96px; letter-spacing: 0;
  }
  .price-card {
    position: absolute; top: 777px; width: 362px; height: 237px;
    border-radius: 28px; background: var(--tile); color: var(--navy);
  }
  .price-card:nth-of-type(1) { left: 114px; }
  .price-title {
    position: absolute; left: 0; right: 0; top: 22px; text-align: center;
    font-family: "Bebas Neue", sans-serif; font-size: 58px; line-height: 1;
  }
  .price-old {
    position: absolute; left: 26px; top: 84px;
    font-family: "Bebas Neue", sans-serif; font-size: 46px; line-height: 1;
  }
  .price-old::after {
    content: ""; position: absolute; left: -12px; right: -14px; top: 22px;
    height: 4px; background: var(--red); transform: rotate(-12deg);
  }
  .badge-now {
    position: absolute; left: 35px; top: 137px; width: 74px; height: 74px;
    border-radius: 50%; background: var(--red); color: var(--white);
    display: flex; align-items: center; justify-content: center;
    font-weight: 700; font-size: 21px;
  }
  .price-new {
    position: absolute; left: 124px; top: 78px;
    font-family: "Bebas Neue", sans-serif; font-size: 186px; line-height: 1; letter-spacing: 2px;
  }
  .offer-note {
    position: absolute; left: 112px; top: 1046px;
    font-size: 37px; color: var(--navy); font-weight: 400;
  }
  .offer-note strong { font-weight: 800; }
  .footer-band {
    position: absolute; left: 0; top: 1114px; width: 1740px; height: 110px;
    background: linear-gradient(90deg, #1d469d 0%, #3569b5 60%, #4a7cc4 100%);
    display: flex; align-items: center; padding-left: 112px; gap: 52px;
  }
  .web-link { display: flex; align-items: center; gap: 22px; color: var(--white); font-weight: 700; font-size: 33px; }
  .web-link svg { width: 36px; height: 36px; }
  .delivery-seal {
    position: absolute; left: 1254px; top: 756px; width: 444px; height: 444px;
    border-radius: 50%; background: var(--red); border: 18px solid var(--white);
    color: var(--white); text-align: center;
    display: flex; flex-direction: column; align-items: center; justify-content: center;
    font-weight: 800;
  }
  .delivery-seal .big { font-size: 60px; line-height: 1.1; }
  .delivery-seal .small { font-size: 37px; line-height: 1.3; margin-top: 8px; margin-bottom: 40px; font-weight: 700; }
</style>
</head>
<body>
<div class="stage">
  <div class="ad">
    <div class="hero-photo" role="img" aria-label="Foto: Person in Gummistiefeln reinigt einen roten Orientteppich mit dem Hochdruckreiniger"></div>

    <svg class="brand-panel" viewBox="0 0 760 525" aria-hidden="true">
      <defs>
        <linearGradient id="panelFill" x1="0" y1="0" x2="1" y2="1">
          <stop offset="0" stop-color="#0a3fb5"/>
          <stop offset="1" stop-color="#2a74dd"/>
        </linearGradient>
      </defs>
      <polygon points="0,0 590,0 758,525 0,525" fill="url(#panelFill)"/>
      <circle cx="616" cy="333" r="8" fill="#fff"/>
      <circle cx="584" cy="386" r="11" fill="#fff"/>
      <circle cx="680" cy="398" r="4" fill="#fff"/>
      <circle cx="653" cy="442" r="18" fill="#fff"/>
      <circle cx="547" cy="472" r="16" fill="#fff"/>
    </svg>
    <div class="brand-name">KWR<br>Teppichservice<br>GmbH</div>

    <div class="photo-round one" role="img" aria-label="Foto: Hochdruckreinigung eines roten Teppichs mit Schaum"></div>
    <div class="photo-round two" role="img" aria-label="Foto: Teppichreinigungsmaschine schäumt einen roten Teppich ein"></div>

    <h1 class="headline">Teppichreinigung<br>&amp; Teppichreparatur</h1>

    <div class="price-card" style="left:114px">
      <div class="price-title">Normalwäsche</div>
      <div class="price-old">19€</div>
      <div class="badge-now">Jetzt</div>
      <div class="price-new">16€</div>
    </div>
    <div class="price-card" style="left:498px">
      <div class="price-title">Vollwäsche</div>
      <div class="price-old">27€</div>
      <div class="badge-now">Jetzt</div>
      <div class="price-new">24€</div>
    </div>
    <div class="price-card" style="left:882px">
      <div class="price-title">Seidenwäsche</div>
      <div class="price-old">49€</div>
      <div class="badge-now">Jetzt</div>
      <div class="price-new">40€</div>
    </div>

    <p class="offer-note">angebot gilt nur <strong>5 Tage</strong> vom xx.xx.xx bis zum xx.xx.xx</p>

    <div class="footer-band">
      <span class="web-link">
        <svg viewBox="0 0 36 36" aria-hidden="true"><circle cx="18" cy="18" r="17" fill="#fff"/><g fill="none" stroke="#2f5fae" stroke-width="2"><circle cx="18" cy="18" r="10"/><ellipse cx="18" cy="18" rx="4.5" ry="10"/><line x1="8" y1="18" x2="28" y2="18"/><line x1="10" y1="13" x2="26" y2="13"/><line x1="10" y1="23" x2="26" y2="23"/></g></svg>
        www.kwr-teppichservice.de
      </span>
      <span class="web-link">
        <svg viewBox="0 0 36 36" aria-hidden="true"><circle cx="18" cy="18" r="17" fill="#fff"/><g fill="none" stroke="#2f5fae" stroke-width="2"><circle cx="18" cy="18" r="10"/><ellipse cx="18" cy="18" rx="4.5" ry="10"/><line x1="8" y1="18" x2="28" y2="18"/><line x1="10" y1="13" x2="26" y2="13"/><line x1="10" y1="23" x2="26" y2="23"/></g></svg>
        www.teppiche-morandi.de
      </span>
    </div>

    <div class="delivery-seal">
      <div class="big">Kostenlose</div>
      <div class="small">Abholung und<br>lieferung</div>
    </div>
  </div>
</div>
</body>
</html>
```